Property investment company needs a letterhead design!

We are a new residential and commercial property investment company. Name of the company is Morvesta Group, LLC. We have a new logo and now we need letterhead! We prefer to have a professional and upscale appearance. We don't have any fixed requirements, so be creative! Thank you for considering this project. We are so excited to see what happens!

Target Market(s)

Professional

Industry/Entity Type

Real Estate Development

```html
<!DOCTYPE html>
<html lang="en">
<head>
<meta charset="utf-8">
<title>Morvesta Group, LLC — Letterhead</title>
<link rel="stylesheet" href="https://fonts.googleapis.com/css2?family=Open+Sans:wght@400;600;700;800&display=swap">
<style>
  :root {
    --navy: #0a1f3d;
    --sky: #1aa3e8;
    --ink: #222b36;
    --muted: #4a525c;
    --backdrop: #e9eaec;
    --paper: #ffffff;
    --watermark: #f2f3f5;
  }
  * { box-sizing: border-box; margin: 0; padding: 0; }
  html, body {
    width: 1200px; height: 1200px; overflow: hidden;
    background: var(--backdrop);
    font-family: "Open Sans", Arial, sans-serif;
  }
  .letterhead {
    position: absolute; left: 245px; top: 78px;
    width: 743px; height: 1043px;
    background: var(--paper);
    overflow: hidden;
  }
  .brand {
    position: absolute; left: 38px; top: 50px;
    display: flex; align-items: center; gap: 8px;
    color: var(--navy); font-weight: 800; font-size: 16px; line-height: 1.15;
    letter-spacing: 0.3px; white-space: nowrap;
  }
  .brand-dot { width: 12px; height: 12px; border-radius: 50%; background: var(--navy); flex: none; }
  .skyline {
    position: absolute; left: 220px; top: 17px; width: 523px; height: 110px;
    background: linear-gradient(to bottom, rgba(26,163,232,0.55), rgba(160,210,240,0.15));
  }
  .header-rule { position: absolute; left: 0; top: 131px; width: 743px; height: 14px; }
  .rule-bar { position: absolute; top: 0; height: 13px; background: var(--navy); }
  .rule-bar.left { left: 0; width: 131px; }
  .rule-bar.right { left: 608px; width: 135px; }
  .rule-dash {
    position: absolute; left: 131px; width: 477px; top: 6px;
    border-top: 1.5px dashed var(--navy);
  }
  .recipient { position: absolute; left: 97px; top: 191px; }
  .recipient-name { color: var(--sky); font-weight: 600; font-size: 12.5px; }
  .recipient-position { color: var(--muted); font-size: 9.5px; margin-top: 2px; }
  .date { position: absolute; left: 608px; top: 191px; color: var(--ink); font-weight: 600; font-size: 11.5px; }
  .watermark-name {
    position: absolute; left: 0; width: 743px; top: 520px; text-align: center;
    color: var(--watermark); font-weight: 800; font-size: 74px; letter-spacing: 2px;
  }
  .contact { position: absolute; left: 95px; top: 863px; list-style: none; }
  .contact li { display: flex; align-items: center; height: 37px; margin-bottom: 4px; }
  .contact-icon {
    width: 37px; height: 37px; flex: none; display: flex;
    align-items: center; justify-content: center; background: var(--sky);
  }
  .contact-icon.dark { background: var(--navy); }
  .contact-text { margin-left: 14px; color: var(--ink); font-size: 12px; line-height: 16px; }
  .footer-band { position: absolute; left: 0; top: 1005px; width: 743px; height: 38px; background: var(--navy); }
  .footer-accent {
    position: absolute; left: 560px; top: 991px; width: 183px; height: 8px;
    background: var(--sky);
    clip-path: polygon(8px 0, 100% 0, 100% 100%, 0 100%);
  }
</style>
</head>
<body>
  <main class="letterhead">
    <div class="brand"><span class="brand-dot"></span><span>MORVESTA<br>GROUP, LLC</span></div>
    <div class="skyline" role="img" aria-label="Pixelated blue city skyline illustration"></div>

    <div class="header-rule">
      <span class="rule-bar left"></span>
      <span class="rule-dash"></span>
      <span class="rule-bar right"></span>
    </div>

    <div class="recipient">
      <p class="recipient-name">Name</p>
      <p class="recipient-position">Position</p>
    </div>
    <p class="date">Date:</p>

    <p class="watermark-name" aria-hidden="true">MORVESTA</p>

    <ul class="contact">
      <li>
        <span class="contact-icon">
          <svg width="22" height="22" viewBox="0 0 24 24"><path fill="#fff" d="M6.6 10.8c1.4 2.8 3.8 5.1 6.6 6.6l2.2-2.2c.3-.3.7-.4 1-.2 1.1.4 2.3.6 3.6.6.6 0 1 .4 1 1V20c0 .6-.4 1-1 1C10.6 21 3 13.4 3 4c0-.6.4-1 1-1h3.5c.6 0 1 .4 1 1 0 1.3.2 2.5.6 3.6.1.3 0 .7-.2 1z"/></svg>
        </span>
        <span class="contact-text">+000 12345 6789<br>+000 12345 6789</span>
      </li>
      <li>
        <span class="contact-icon dark">
          <svg width="22" height="22" viewBox="0 0 24 24" fill="none" stroke="#fff" stroke-width="1.5"><circle cx="12" cy="12" r="9"/><ellipse cx="12" cy="12" rx="4" ry="9"/><path d="M3 12h18M5 7h14M5 17h14"/></svg>
        </span>
        <span class="contact-text">urwebsitename.com<br>urname@email.com</span>
      </li>
      <li>
        <span class="contact-icon">
          <svg width="22" height="22" viewBox="0 0 24 24"><path fill="#fff" d="M12 2a6 6 0 0 0-6 6c0 4.5 6 11 6 11s6-6.5 6-11a6 6 0 0 0-6-6zm0 8.2A2.2 2.2 0 1 1 12 5.8a2.2 2.2 0 0 1 0 4.4z"/><ellipse cx="12" cy="20.5" rx="6" ry="1.6" fill="none" stroke="#fff" stroke-width="1.2"/></svg>
        </span>
        <span class="contact-text">Street Address Here</span>
      </li>
    </ul>

    <div class="footer-accent"></div>
    <div class="footer-band"></div>
  </main>
</body>
</html>
```